Existing WP site needs a fresh look (design only)

The current website, www.quorrahub.com.au, is fine, but needs a fresh look so their clients can tell their website has been 'refreshed' regularly.
https://www.quorrahub.com.au/sitemap/
They will use the existing functionality.
They want to keep the blue, green and white of their logo as the main colors, but a fresh look. They prefer a light look to a dark look, but they would be open to good designs that change their mind.
Be creative, think outside the box.
You only need to supply the 'home page ' design to win but the winners will be asked to provide an extra 'standard' page template (like the one currently being used for search results and other pages)
Any photos used must be supplied without charge with the PSDs in a resolution acceptable for the WordPress site.

```html
<!DOCTYPE html>
<html lang="en">
<head>
<meta charset="utf-8">
<title>Quorra Hub – Home</title>
<link href="https://fonts.googleapis.com/css2?family=Roboto:wght@400;500;700&display=swap" rel="stylesheet">
<style>
:root{
  --green:#6db52e;
  --green-dark:#4f8a1c;
  --ink:#0c0c0c;
  --panel:#151515;
  --band:#1b1b1b;
  --white:#ffffff;
  --muted:#cfcfcf;
}
*{box-sizing:border-box;margin:0;padding:0}
html,body{width:1200px;height:1200px;overflow:hidden;background:#1a1a1a;font-family:'Roboto',sans-serif;color:var(--white)}
.stage{position:relative;width:1200px;height:1200px}
.page{position:absolute;left:371px;top:0;width:530px;height:1390px;transform:scale(.8633);transform-origin:0 0;background:var(--ink);overflow:hidden}
.abs{position:absolute}
.hero-bg{left:0;top:0;width:530px;height:280px;background:radial-gradient(ellipse at 30% 40%,#2a2a2a,#0c0c0c 70%)}
.logo{left:19px;top:25px;font-size:15px;font-weight:700;display:flex;align-items:center;gap:5px}
.logo .mark{width:10px;height:10px;background:var(--green)}
.nav{right:22px;top:30px;display:flex;gap:16px;font-size:8px;font-weight:500}
.tagline{left:19px;top:69px;font-size:7.5px;font-weight:700}
.contact-box{background:linear-gradient(90deg,rgba(109,181,46,0),var(--green) 35%);display:flex;align-items:center;justify-content:flex-end;gap:10px;padding-right:10px;font-size:6px;font-weight:500;line-height:1.6}
.contact-box svg{flex:none}
.contact-box table{border-spacing:0}
.contact-box td{padding:0 3px}
.search-bar{left:235px;top:132px;width:272px;height:26px;background:linear-gradient(90deg,rgba(109,181,46,0),var(--green) 60%);display:flex;align-items:center;justify-content:flex-end;gap:8px;padding-right:8px;font-size:7px}
.or{left:366px;top:173px;font-size:7px}
.select{width:129px;height:25px;border:1px solid var(--green);border-radius:2px;font-size:7px;display:flex;align-items:center;justify-content:space-between;padding:0 10px}
.select::after{content:"";width:4px;height:4px;border-right:1px solid #fff;border-bottom:1px solid #fff;transform:rotate(45deg) translateY(-2px)}
.btn-search{left:306px;top:317px;width:128px;height:25px;background:var(--green);font-size:7px;font-weight:700;display:flex;align-items:center;justify-content:center}
.hero-title{left:22px;top:148px;font-size:33px;font-weight:700;line-height:1.25}
.hero-sub{left:22px;top:237px;font-size:16px;font-weight:700}
.band{left:19px;width:275px;height:25px;background:linear-gradient(90deg,var(--green),rgba(109,181,46,0));font-size:12px;font-weight:700;display:flex;align-items:center;padding-left:13px}
.section-bg{left:0;width:530px;background:radial-gradient(ellipse at 50% 40%,#222,#0c0c0c 70%)}
.arrow{width:17px;height:17px;border-radius:50%;background:var(--green);display:flex;align-items:center;justify-content:center}
.card{top:467px;width:110px;height:145px;background:var(--green);border-radius:4px;text-align:center;padding:66px 8px 0;font-size:6.5px}
.card h3{font-size:7px;font-weight:700;line-height:1.3}
.card p{font-size:5.2px;line-height:1.35;text-align:justify;margin-top:5px}
.card .demo{position:absolute;left:0;right:0;bottom:8px;font-size:5.5px;display:flex;justify-content:center;align-items:center;gap:8px}
.play{width:8px;height:8px;border-radius:50%;background:#fff;position:relative}
.play::after{content:"";position:absolute;left:3px;top:2px;border-left:3px solid var(--green);border-top:2px solid transparent;border-bottom:2px solid transparent}
.avatar{top:435px;width:90px;height:90px;border-radius:50%;border:2px solid var(--green)}
.news-img{top:760px;width:146px;height:90px;border:3px solid var(--green);border-radius:3px}
.news-cap{top:859px;width:160px;text-align:center;font-size:7px;font-weight:500}
.read-more{top:877px;width:36px;height:12px;background:var(--green);font-size:5px;display:flex;align-items:center;justify-content:center}
.testi{top:1001px;width:122px}
.testi-head{height:18px;background:var(--green);padding:2px 0 0 24px;font-size:5.5px;line-height:1.2}
.testi-head small{display:block;font-size:4px}
.testi-body{height:48px;background:linear-gradient(180deg,var(--green-dark),rgba(79,138,28,0));font-size:5.3px;line-height:1.35;padding:6px 10px 0 14px}
.badge{top:996px;width:28px;height:28px;border-radius:50%;background:#fff;border:2px solid var(--green);font-size:5px;font-weight:700;color:var(--ink);display:flex;align-items:center;justify-content:center}
.clients{left:19px;top:1161px;width:492px;display:flex;justify-content:space-between;align-items:center;font-size:9px;font-weight:500}
.footer-logo{left:19px;top:1230px;font-size:30px;font-weight:700;line-height:1;display:flex;gap:8px;align-items:center}
.footer-logo .mark{width:22px;height:22px;background:var(--green)}
.follow{left:170px;top:1228px;font-size:9px;font-weight:500}
.social{left:178px;top:1254px;display:grid;grid-template-columns:46px 46px;gap:16px 4px;font-size:7px}
.copyright{left:0;top:1345px;width:530px;text-align:center;font-size:5.5px}
</style>
</head>
<body>
<div class="stage">
<main class="page">
  <div class="abs hero-bg" role="img" aria-label="Dark studio photograph of a microphone"></div>
  <div class="abs logo"><span>Quorra Hub</span><span class="mark"></span></div>
  <nav class="abs nav"><span>Voices</span><span>Rate</span><span>Payment</span><span>News</span><span>About Us</span><span>Contact</span><span>Shortlist</span></nav>
  <div class="abs tagline">JUST SAY THE WORD</div>

  <div class="abs contact-box" style="left:355px;top:70px;width:152px;height:36px">
    <svg width="14" height="18" viewBox="0 0 14 18"><rect x="1" y="1" width="9" height="16" rx="1.5" fill="none" stroke="#fff" stroke-width="1.5"/><path d="M12 6q2 3 0 6" fill="none" stroke="#fff"/></svg>
    <table><tr><td>Melbourne</td><td>:</td><td>+ 61 3 9000 4182</td></tr><tr><td>Sydney</td><td>:</td><td>+ 61 2 9000 7316</td></tr></table>
  </div>

  <h1 class="abs hero-title">Australia's<br>Top Voices</h1>
  <div class="abs hero-sub">Professional Casting</div>

  <div class="abs search-bar"><span>Search artists...</span>
    <svg width="12" height="12" viewBox="0 0 12 12"><circle cx="5" cy="5" r="3.8" fill="none" stroke="#fff" stroke-width="1.5"/><path d="M8 8l3.5 3.5" stroke="#fff" stroke-width="1.5"/></svg></div>
  <div class="abs or">or</div>
  <div class="abs select" style="left:233px;top:209px">Location</div>
  <div class="abs select" style="left:378px;top:209px">Language</div>
  <div class="abs select" style="left:233px;top:245px">Talent Range</div>
  <div class="abs select" style="left:378px;top:245px">Age Range</div>
  <div class="abs select" style="left:233px;top:281px">Sex</div>
  <div class="abs select" style="left:378px;top:281px">Accent</div>
  <div class="abs btn-search">SEARCH</div>

  <div class="abs section-bg" style="top:360px;height:270px"></div>
  <div class="abs band" style="top:377px">Spotlight</div>
  <div class="abs arrow" style="left:30px;top:515px"><svg width="6" height="8"><path d="M5 1L2 4l3 3" fill="none" stroke="#fff" stroke-width="1.5"/></svg></div>
  <div class="abs arrow" style="left:478px;top:515px"><svg width="6" height="8"><path d="M1 1l3 3-3 3" fill="none" stroke="#fff" stroke-width="1.5"/></svg></div>

  <div class="abs card" style="left:81px"><h3>Mara Ellison<br>Artist - Melbourne</h3><p>Mara has a natural warmth and freshness in her voice, as well as an intelligence and truthfulness to her phrasing</p><div class="demo"><span class="play"></span>2020 Demo</div></div>
  <div class="abs card" style="left:208px"><h3>Clare Dunmore<br>Artist - Melbourne</h3><p>Whether it be long form narration, intimate lures, snappy retail, or beyond – Clare loves nothing more than bringing a script to life.</p><div class="demo"><span class="play"></span>2020 Demo</div></div>
  <div class="abs card" style="left:335px"><h3>Jesse Arden<br>Artist - Sydney</h3><p>Hi my name is Jesse. Born 2003 and have know been a voice over artist with Quorra Hub since I was 6 years old.</p><div class="demo"><span class="play"></span>2018 Demo</div></div>
  <div class="abs avatar" style="left:91px;background:radial-gradient(circle at 50% 40%,#e9e4df,#9a958f)" role="img" aria-label="Portrait photo of voice artist Mara Ellison"></div>
  <div class="abs avatar" style="left:218px;background:radial-gradient(circle at 50% 45%,#c98f74,#4a2418)" role="img" aria-label="Portrait photo of voice artist Clare Dunmore"></div>
  <div class="abs avatar" style="left:345px;background:radial-gradient(circle at 50% 45%,#b98c70,#2e3a3e)" role="img" aria-label="Portrait photo of voice artist Jesse Arden"></div>

  <div class="abs section-bg" style="top:700px;height:230px"></div>
  <div class="abs band" style="top:673px">News</div>
  <div class="abs arrow" style="left:54px;top:797px"><svg width="6" height="8"><path d="M5 1L2 4l3 3" fill="none" stroke="#fff" stroke-width="1.5"/></svg></div>
  <div class="abs arrow" style="left:455px;top:797px"><svg width="6" height="8"><path d="M1 1l3 3-3 3" fill="none" stroke="#fff" stroke-width="1.5"/></svg></div>
  <div class="abs news-img" style="left:108px;background:linear-gradient(90deg,#d8d8d8,#6a6a6a,#d0d0d0,#5c5c5c)" role="img" aria-label="Black and white photo of voice artist Luke Varran"></div>
  <div class="abs news-img" style="left:272px;background:linear-gradient(135deg,#5f7378,#a58068,#3b4a4e)" role="img" aria-label="Photo of voice artist Owen Pratley"></div>
  <div class="abs news-cap" style="left:101px">NEW VOICE ALERT | Luke Varran</div>
  <div class="abs news-cap" style="left:265px">NEW VOICE ALERT | Owen Pratley</div>
  <div class="abs read-more" style="left:163px">Read More</div>
  <div class="abs read-more" style="left:327px">Read More</div>

  <div class="abs band" style="top:951px">Testimonials</div>
  <div class="abs arrow" style="left:42px;top:1023px"><svg width="6" height="8"><path d="M5 1L2 4l3 3" fill="none" stroke="#fff" stroke-width="1.5"/></svg></div>
  <div class="abs arrow" style="left:466px;top:1023px"><svg width="6" height="8"><path d="M1 1l3 3-3 3" fill="none" stroke="#fff" stroke-width="1.5"/></svg></div>
  <div class="abs testi" style="left:106px"><div class="testi-head">Streamly<small>Tom Rell, Creative Director</small></div><div class="testi-body">Our business pushes the boundaries of 'tight deadlines' to new levels, and the team at Quorra Hub save our bacon on a weekly basis.</div></div>
  <div class="abs testi" style="left:287px"><div class="testi-head">Loomwear<small>Neil Carver, Creative Director</small></div><div class="testi-body">Using Quorra Hub means we can offer a unique array of high-end talented voice over artists that can cover any brief our clients need.</div></div>
  <div class="abs badge" style="left:96px">SM</div>
  <div class="abs badge" style="left:277px">LW</div>

  <div class="abs band" style="top:1105px">Clients</div>
  <div class="clients abs"><span>Ridgeway</span><span>Lumelle</span><span>Burgerlane</span><span>Northcast</span><span>Clearsight</span><span>Cocoaleaf</span><span>Unova</span><span>Tristar</span></div>

  <div class="abs footer-logo"><span>Quorra<br>Hub</span><span class="mark"></span></div>
  <div class="abs follow">Follow us @quorrahub</div>
  <div class="abs social"><span>Chatter</span><span>Pinline</span><span>Snapbook</span><span>Linkwork</span></div>
  <div class="abs contact-box" style="left:330px;top:1223px;width:177px;height:35px">
    <svg width="14" height="18" viewBox="0 0 14 18"><rect x="1" y="1" width="9" height="16" rx="1.5" fill="none" stroke="#fff" stroke-width="1.5"/><path d="M12 6q2 3 0 6" fill="none" stroke="#fff"/></svg>
    <table><tr><td>Melbourne</td><td>:</td><td>+ 61 3 9000 4182</td></tr><tr><td>Sydney</td><td>:</td><td>+ 61 2 9000 7316</td></tr></table>
  </div>
  <div class="abs contact-box" style="left:330px;top:1272px;width:177px;height:35px;text-align:right;gap:18px">
    <svg width="10" height="13" viewBox="0 0 10 13"><path d="M5 12C2 8 1 6 1 4.5a4 4 0 018 0C9 6 8 8 5 12z" fill="#fff"/><circle cx="5" cy="4.5" r="1.5" fill="#6db52e"/></svg>
    <div style="line-height:1.45">Quorra Hub Pty Limited<br>Suite 14, 60 Harlow Lane Redfern<br>NSW 2016 Australia</div>
  </div>
  <div class="abs copyright">© Copyright 2018 Quorra Hub Pty Limited. Privacy Policy &amp; Terms and Conditions | Sitemap</div>
</main>
</div>
</body>
</html>
```